Business Card Design Project

We need a simple business card design that uses our current logo.
We need to have the current logo put into a high res format.
We need to have 1 card made with contact information.
We will supply the information for the 4 employees.
Industry/Entity Type
Business
Requirements
Must have
- The contact information is as follows:
Paul Vardenko
Producer/CEO
c. 949-555-0148
f. 650-555-0193
paulv@lanternyardstudio.example
Mel Trosgaard, CFO
c. 949-555-0172
f. 650-555-0193
melt@lanternyardstudio.example
Paul Brenneky, PR
c. 267-555-0126
f. 650-555-0193
pbrenneky@lanternyardstudio.example
Dale Furnow, Producer
c. 949-555-0164
f. 650-555-0193
dalef@lanternyardstudio.example
The address for all cards is:
318 W Calle Norvista #2715, San Clemente, CA 92631

```html
<!DOCTYPE html>
<html lang="en">
<head>
<meta charset="utf-8">
<title>Lantern Yard Studio – Business Card</title>
<link rel="stylesheet" href="https://fonts.googleapis.com/css2?family=Open+Sans:wght@400;600;700&display=swap">
<style>
  :root {
    --page-bg: #ece7df;
    --card-blue: #1177c2;
    --card-red: #c1272b;
    --card-maroon: #731913;
    --text-light: #ffffff;
    --text-soft: #e9f2fa;
    --card-shadow: rgba(40, 25, 10, 0.35);
  }
  * { box-sizing: border-box; margin: 0; padding: 0; }
  html, body {
    width: 1200px;
    height: 1000px;
    overflow: hidden;
    background: var(--page-bg);
    font-family: "Open Sans", Arial, sans-serif;
  }
  .sheet {
    position: relative;
    width: 1200px;
    height: 1000px;
  }
  .card {
    position: absolute;
    top: 349px;
    width: 537px;
    height: 302px;
    border-radius: 8px;
    overflow: hidden;
    box-shadow: 0 4px 10px var(--card-shadow);
  }
  .card--front { left: 47px; }
  .card--back { left: 617px; }
  .card__art {
    position: absolute;
    inset: 0;
    width: 100%;
    height: 100%;
    display: block;
  }
  .fill-blue { fill: var(--card-blue); }
  .fill-red { fill: var(--card-red); }
  .fill-maroon { fill: var(--card-maroon); }

  .brand-name {
    position: absolute;
    color: var(--text-light);
    font-weight: 700;
    text-transform: uppercase;
    white-space: nowrap;
    line-height: 1.2;
  }
  .card--front .brand-name {
    left: 22px;
    top: 196px;
    font-size: 18px;
    letter-spacing: 0.5px;
    transform-origin: left top;
    transform: rotate(-46deg);
  }
  .card--back .brand-name {
    left: 0;
    right: 0;
    top: 138px;
    text-align: center;
    font-size: 20px;
    letter-spacing: 1px;
  }

  .contact-list {
    position: absolute;
    left: 214px;
    top: 122px;
    list-style: none;
    transform-origin: left top;
    transform: rotate(-46deg);
    color: var(--text-soft);
    font-size: 10px;
    line-height: 18px;
    white-space: nowrap;
  }
  .contact-list__item {
    display: flex;
    align-items: center;
    height: 18px;
  }
  .contact-list__icon {
    width: 16px;
    display: inline-flex;
    justify-content: center;
    margin-right: 5px;
    color: var(--text-light);
  }
  .contact-list__icon svg { display: block; fill: var(--text-light); }
  .contact-list__icon--at { font-weight: 700; font-size: 13px; }

  .person {
    position: absolute;
    left: 180px;
    top: 150px;
    transform-origin: left top;
    transform: rotate(43deg);
    color: var(--text-light);
    white-space: nowrap;
  }
  .person__name {
    font-size: 15px;
    font-weight: 700;
    line-height: 19px;
  }
  .person__title {
    font-size: 12px;
    font-weight: 400;
    line-height: 15px;
    margin-left: -4px;
    color: var(--text-soft);
  }
</style>
</head>
<body>
<main class="sheet">

  <section class="card card--front" aria-label="Business card front">
    <svg class="card__art" viewBox="0 0 537 302" preserveAspectRatio="none" aria-hidden="true">
      <rect class="fill-red" x="0" y="0" width="537" height="302"/>
      <polygon class="fill-blue" points="298,0 537,0 537,302 366,302 195,118"/>
      <polygon class="fill-maroon" points="195,118 366,302 28,302"/>
    </svg>

    <div class="brand-name">Lantern Yard Studio</div>

    <ul class="contact-list">
      <li class="contact-list__item">
        <span class="contact-list__icon">
          <svg width="8" height="11" viewBox="0 0 9 12"><rect x="0" y="0" width="9" height="12" rx="1.5"/><rect x="2" y="2" width="5" height="5" fill="#1177c2"/></svg>
        </span>949-555-0148
      </li>
      <li class="contact-list__item">
        <span class="contact-list__icon">
          <svg width="11" height="11" viewBox="0 0 24 24"><path d="M6.6 10.8a15.1 15.1 0 0 0 6.6 6.6l2.2-2.2c.3-.3.7-.4 1-.2 1.1.4 2.3.6 3.6.6.6 0 1 .4 1 1V20c0 .6-.4 1-1 1A17 17 0 0 1 3 4c0-.6.4-1 1-1h3.5c.6 0 1 .4 1 1 0 1.3.2 2.5.6 3.6.1.3 0 .7-.2 1z"/></svg>
        </span>650-555-0193
      </li>
      <li class="contact-list__item">
        <span class="contact-list__icon contact-list__icon--at">@</span>paulv@lanternyardstudio.example
      </li>
      <li class="contact-list__item">
        <span class="contact-list__icon">
          <svg width="9" height="12" viewBox="0 0 24 30"><path d="M12 0a10 10 0 0 0-10 10c0 7.5 10 20 10 20s10-12.5 10-20A10 10 0 0 0 12 0zm0 14a4 4 0 1 1 0-8 4 4 0 0 1 0 8z"/></svg>
        </span>318 W Calle Norvista #2715
      </li>
      <li class="contact-list__item">
        <span class="contact-list__icon"></span>San Clemente, CA 92631
      </li>
    </ul>

    <div class="person">
      <p class="person__name">Paul Vardenko</p>
      <p class="person__title">Producer/CEO</p>
    </div>
  </section>

  <section class="card card--back" aria-label="Business card back">
    <svg class="card__art" viewBox="0 0 537 302" preserveAspectRatio="none" aria-hidden="true">
      <rect class="fill-blue" x="0" y="0" width="537" height="302"/>
      <polygon class="fill-red" points="388,0 537,0 537,150"/>
      <polygon class="fill-maroon" points="0,152 0,302 152,302"/>
    </svg>
    <div class="brand-name">Lantern Yard Studio</div>
  </section>

</main>
</body>
</html>
```